Simple, Elegant, Clean Homepage Design For Jobrova.com - for job seekers.

Hello, we're going to start this site by posting a project for ONE page of it - the homepage. I've attached a simple wireframe I created and we'll be using logo #1 in the attached PDF.

Anyway, all the wireframe shows is where the elements should be. You'll put in placeholder image(s) where needed. (i.e. The BrightDesk banner.)

We are looking for a simple, clean site - very minimalistic but also one that grabs the eye.

Simple, clean menu across the top...the little links at the bottom...

And in the middle show us some headline styles, subhead styles, body copy font style, and bullets we can use.

As you can see there is also a search tool for employers in the upper right, so we'd like to see your vision of that as well.

Thanks!

Tom

P.S. You can just put in some garbled example text to illustrate fonts and other elements listed in the description.

P.P.S. I just added a new PDF to this project showing some updated tag lines we like with the "jobrova.com/your-name-here" thing we like. See if this can be integrated into your existing designs - or new designs.

Target Market(s)

Job Seekers

Number of Pages Required

1 page

Font styles to use
Sans Serif

Colors
ffffff
0456a4
000000
c5c5c5

Requirements
Must have
• Must be a simple, clean, optimized HTML/CSS design. We are looking for a minimalistic approach, so that we can easily highlight certain features/text/icons with color.
Nice to have
• White background, elegant and "soft" outlines for sections, easy to read font, headline fonts/colors that grab, tasteful bullets.
Should not have
• Complex design
• hard to read fonts
• busy/loud design
• not too serious, not too casual

```html
<!DOCTYPE html>
<html lang="en">
<head>
<meta charset="utf-8">
<title>Jobrova — Homepage</title>
<link rel="stylesheet" href="https://fonts.googleapis.com/css2?family=Montserrat:ital,wght@0,400;0,500;0,600;0,700;0,900;1,400;1,500&family=Barlow+Condensed:ital,wght@1,500&display=swap">
<style>
  :root {
    --white: #ffffff;
    --black: #000000;
    --cyan: #1fb3d8;
    --blue: #0456a4;
    --button-blue: #0c8fc1;
    --orange: #ff9f40;
    --bullet-orange: #f7953b;
    --panel-grey: #ebebeb;
    --field-grey: #c5c5c5;
    --field-pale: #e4f5fb;
    --placeholder: #a7cfdc;
    --muted: #6b6b6b;
  }
  * { box-sizing: border-box; margin: 0; padding: 0; }
  html, body { width: 1200px; height: 1200px; overflow: hidden; background: var(--white); }
  body { font-family: "Montserrat", sans-serif; color: var(--black); position: relative; }
  .page { position: absolute; left: 0; top: 35px; width: 1200px; height: 1131px; }
  .page > * { position: absolute; }

  .brand { left: 31px; top: 22px; display: flex; align-items: center; gap: 8px; }
  .brand-dot { width: 30px; height: 30px; border-radius: 50%; background: var(--orange); }
  .brand-name { font-size: 54px; font-weight: 600; color: var(--cyan); letter-spacing: -1px; line-height: 1; }
  .tagline { left: 48px; top: 96px; font-family: "Barlow Condensed", sans-serif; font-style: italic; font-weight: 500; font-size: 20px; }

  .main-nav a { position: absolute; top: 58px; font-size: 17px; font-weight: 500; color: var(--cyan); text-decoration: none; white-space: nowrap; }
  .main-nav .is-active { color: var(--bullet-orange); }

  .employer-search { left: 921px; top: 0; width: 245px; height: 136px; background: var(--orange); border-radius: 0 0 45px 45px; }
  .employer-search h2 { position: absolute; top: 21px; width: 100%; text-align: center; font-size: 17px; font-weight: 500; color: var(--white); }
  .employer-search .search-field { position: absolute; left: 15px; top: 55px; width: 186px; height: 28px; border-radius: 14px; background: var(--field-pale); font-size: 9px; font-style: italic; color: var(--placeholder); padding: 8px 12px; }
  .employer-search .search-button { position: absolute; left: 205px; top: 55px; width: 29px; height: 29px; border-radius: 50%; background: var(--cyan); }

  .hero { left: 30px; top: 146px; width: 823px; height: 361px; background: var(--panel-grey); }
  .headline { left: 76px; top: 160px; font-size: 78px; font-weight: 900; letter-spacing: -1px; line-height: 1; }
  .intro { left: 85px; top: 271px; width: 720px; text-align: center; font-size: 15.5px; line-height: 24.6px; }
  .feature-list { left: 155px; top: 380px; list-style: none; }
  .feature-list li { display: flex; align-items: center; gap: 9px; height: 29px; font-size: 19px; font-weight: 500; color: var(--bullet-orange); }
  .feature-list svg { width: 22px; height: 22px; flex: none; }

  .signin-menu { left: 573px; top: 83px; width: 201px; height: 141px; background: var(--white); border-radius: 8px; box-shadow: 0 2px 8px rgba(0,0,0,.25); }
  .signin-menu .field { position: absolute; left: 13px; width: 174px; height: 27px; background: var(--field-grey); border-radius: 4px; font-size: 9.5px; font-style: italic; color: var(--white); padding: 8px 8px; }
  .signin-menu .submit { position: absolute; left: 13px; top: 80px; width: 174px; height: 27px; background: var(--black); border-radius: 4px; color: var(--white); font-weight: 700; font-size: 12.5px; text-align: center; line-height: 27px; }
  .signin-menu .fine { position: absolute; font-size: 5.5px; font-weight: 600; white-space: nowrap; }
  .signin-menu .fine a { color: var(--button-blue); text-decoration: none; }
  .signin-menu .box { display: inline-block; width: 7px; height: 7px; background: var(--field-grey); vertical-align: middle; margin-right: 3px; }

  .career-line { left: 882px; top: 152px; font-family: "Barlow Condensed", sans-serif; font-style: italic; font-weight: 500; font-size: 19px; white-space: nowrap; }
  .career-line u { color: var(--blue); }
  .career-line sup { font-size: 8px; }
  .profile-url { left: 900px; top: 183px; width: 259px; text-align: right; font-size: 13.5px; color: var(--blue); }

  .signup-card { left: 896px; top: 224px; width: 272px; height: 283px; background: var(--white); border-radius: 16px; box-shadow: 0 1px 7px rgba(0,0,0,.22); }
  .signup-card .field { position: absolute; height: 31px; background: var(--field-pale); border-radius: 3px; font-size: 11px; font-style: italic; color: var(--placeholder); padding: 10px 7px; }
  .signup-card .fine { position: absolute; font-size: 6.5px; color: #b5b5b5; white-space: nowrap; }
  .signup-card .fine b, .signup-card .fine a { color: #444; font-weight: 700; text-decoration: none; }
  .signup-card .fine a { color: var(--button-blue); }
  .signup-card .box { display: inline-block; width: 8px; height: 8px; background: var(--field-grey); vertical-align: middle; margin-right: 6px; }
  .signup-card .submit { position: absolute; left: 92px; top: 206px; width: 87px; height: 27px; background: var(--button-blue); border-radius: 4px; color: var(--white); font-weight: 700; font-size: 14.5px; text-align: center; line-height: 27px; }

  .banner { left: 30px; top: 554px; width: 1136px; height: 381px; background: var(--panel-grey); }

  .site-footer { left: 0; top: 1041px; width: 1200px; height: 55px; background: var(--orange); border-radius: 28px 28px 0 0; }
  .site-footer a { position: absolute; top: 20px; font-size: 12.8px; font-weight: 500; color: var(--white); text-decoration: none; }
  .site-footer .is-active { color: var(--black); }
  .copyright { left: 0; top: 1106px; width: 1200px; text-align: center; font-size: 12px; color: #333; white-space: nowrap; }
  .copyright em { color: var(--muted); }
  .copyright a { color: var(--cyan); text-decoration: none; }
</style>
</head>
<body>
<div class="page">

  <div class="brand"><span class="brand-dot"></span><span class="brand-name">jobrova</span></div>
  <p class="tagline">Because you’re more than just a resume.</p>

  <nav class="main-nav">
    <a href="#" style="left:364px">ABOUT</a>
    <a href="#" style="left:493px">SUPPORT</a>
    <a href="#" class="is-active" style="left:642px">SIGN IN</a>
    <a href="#" style="left:747px">FREE TRAINING</a>
  </nav>

  <section class="employer-search">
    <h2>EMPLOYERS</h2>
    <div class="search-field">Search Candidates</div>
    <div class="search-button">
      <svg viewBox="0 0 29 29" width="29" height="29"><circle cx="16" cy="13" r="4.5" fill="none" stroke="#fff" stroke-width="1.8"/><line x1="12.8" y1="16.2" x2="9" y2="20" stroke="#fff" stroke-width="2" stroke-linecap="round"/></svg>
    </div>
  </section>

  <section class="hero"></section>
  <h1 class="headline">HEADLINE</h1>
  <p class="intro">Lorem ipsum dolor sit amet, consectetur adipiscing elit. Proin blandit ac enim at ultricies. Ut viverra risus at dui sagittis efficitur. Duis ut tortor lorem. Class aptent taciti sociosqu ad litora torquent per conubia nostra, per inceptos himenaeos.</p>
  <ul class="feature-list">
    <li><svg viewBox="0 0 22 22"><circle cx="10" cy="12" r="8.5" fill="none" stroke="#000" stroke-width="2.4"/><path d="M5.5 11.5l4 4L20 3" fill="none" stroke="#1fb3d8" stroke-width="3" stroke-linecap="round"/></svg>Lorem ipsum dolor sit amet, consectetur adipiscing elit.</li>
    <li><svg viewBox="0 0 22 22"><circle cx="10" cy="12" r="8.5" fill="none" stroke="#000" stroke-width="2.4"/><path d="M5.5 11.5l4 4L20 3" fill="none" stroke="#1fb3d8" stroke-width="3" stroke-linecap="round"/></svg>Aliquam semper nisl quis lectus suscipit venenatis.</li>
    <li><svg viewBox="0 0 22 22"><circle cx="10" cy="12" r="8.5" fill="none" stroke="#000" stroke-width="2.4"/><path d="M5.5 11.5l4 4L20 3" fill="none" stroke="#1fb3d8" stroke-width="3" stroke-linecap="round"/></svg>Vestibulum a urna ut justo gravida faucibus at non mi.</li>
  </ul>

  <div class="signin-menu">
    <div class="field" style="top:14px">Username</div>
    <div class="field" style="top:48px">Password</div>
    <div class="submit">SIGN IN</div>
    <p class="fine" style="left:56px;top:113px">New member?</p>
    <p class="fine" style="left:110px;top:112px;font-weight:500"><span class="box"></span>Keep me Signed in</p>
    <p class="fine" style="left:31px;top:124px"><a href="#">Register new account</a></p>
    <p class="fine" style="left:111px;top:124px"><a href="#">Forgot password</a></p>
  </div>

  <p class="career-line">One Amazing <u>Link</u> for the Rest of Your Career.<sup>™</sup></p>
  <p class="profile-url">jobrova.com/YourNameHere</p>

  <form class="signup-card">
    <div class="field" style="left:20px;top:20px;width:111px">First Name</div>
    <div class="field" style="left:140px;top:20px;width:111px">Last Name</div>
    <div class="field" style="left:20px;top:60px;width:231px">Username</div>
    <div class="field" style="left:20px;top:100px;width:231px">Email Address</div>
    <div class="field" style="left:20px;top:140px;width:231px">Password</div>
    <p class="fine" style="left:33px;top:184px">I Agree to the <b>terms of use</b></p>
    <div class="submit">SIGN UP</div>
    <p class="fine" style="left:52px;top:250px"><span class="box"></span>Have an account with us? <a href="#">Login here</a></p>
  </form>

  <div class="banner" role="img" aria-label="Banner image placeholder for the BrightDesk promotion"></div>

  <footer class="site-footer">
    <a href="#" class="is-active" style="left:301px">CONTACT</a>
    <a href="#" style="left:409px">TERMS</a>
    <a href="#" style="left:489px">DISCLAIMER</a>
    <a href="#" style="left:610px">PRIVACY</a>
    <a href="#" style="left:709px">SIGN IN</a>
    <a href="#" style="left:798px">DIRECTORY</a>
  </footer>
  <p class="copyright"><em>Copyright © 2017 Jobrova.</em> Use of this website constitutes acceptance of our <a href="#">User Agreement and Privacy Policy.</a></p>

</div>
</body>
</html>
```